Website redesign for PR company

We currently have a Squarespace site, which has been sufficient during the start up stage of our public relations business. I would be interested to know whether there are options within the Squarespace functionality to dramatically improve the look of our site, or whether you recommend a full redesign using another web service.

I would like the designer to offer some suggestions for improvements to the current site and/or provide designs for a new site.

I would like for us to have an ongoing relationship keeping our site up to date. Our current site is at www.vorlo.co.nz

Target Market(s)

New Zealand primarily, government and commercial clients

Industry/Entity Type

public relations

Coding

Coded - Design and coding required

Number of Pages Required

5+ page

Requirements
Must have
• Vorlo Blue: R38 G34 B98 / #262261 / C100 M100 Y25 K25 Vorlo Orange: R247 G148 B29 / #f7931d / C0 M50 Y100 K0 Pink: R249 G181 B178 / #f8b4b2 / C0 M25 Y25 K0No stock imagery, use of our profile photos as on current site and custom graphics only.
Should not have
• stock images

```html
<!DOCTYPE html>
<html lang="en">
<head>
<meta charset="utf-8">
<title>Vorlo — People With Expertise</title>
<link rel="stylesheet" href="https://fonts.googleapis.com/css2?family=Playfair+Display:wght@500;600;700&family=Poppins:ital,wght@0,400;0,500;0,600;1,400&display=swap">
<style>
:root{
  --navy:#262261;
  --navy-deep:#221e58;
  --orange:#f7931d;
  --pink:#f8b4b2;
  --pink-bg:#efaba7;
  --blush:#fdf2f2;
  --ink:#1f1d3d;
  --muted:#44435a;
  --white:#ffffff;
  --line:#e6e1ea;
}
*{box-sizing:border-box;margin:0;padding:0}
html,body{width:1200px;height:4370px;overflow:hidden}
body{font-family:"Poppins",sans-serif;color:var(--ink);background:var(--white);position:relative}
.abs{position:absolute}
section,header,footer{position:absolute;left:0;width:1200px}
.accent{color:var(--pink)}

/* hero */
.hero{top:0;height:625px;background:var(--navy);color:var(--white)}
.brand{left:102px;top:44px;font-family:"Playfair Display",serif;font-weight:700;font-size:54px;color:var(--white);letter-spacing:-1px}
.menu-btn{left:1054px;top:17px;width:49px;height:41px;border:2px solid var(--white);border-radius:4px;padding:10px 11px;display:flex;flex-direction:column;justify-content:space-between}
.menu-btn span{display:block;height:2px;background:var(--white)}
.hero h1{left:100px;top:252px;font-family:"Playfair Display",serif;font-weight:600;font-size:60px;line-height:1}
.hero .rule{left:100px;top:428px;width:80px;height:3px;background:var(--white)}
.hero p{left:100px;top:446px;width:570px;font-size:15.5px;line-height:33px}
.down{left:570px;top:595px;width:60px;height:60px;border-radius:50%;background:var(--white);box-shadow:0 0 0 5px rgba(38,34,97,.25),0 4px 12px rgba(0,0,0,.15);display:flex;align-items:center;justify-content:center;z-index:2}

/* news */
.news{top:625px;height:531px;background:var(--white)}
.dot{width:20px;height:20px;border-radius:50%;background:var(--pink)}
.section-title{font-family:"Playfair Display",serif;font-weight:500;font-size:32px;color:var(--ink)}
.news .dot{left:100px;top:82px}
.news .section-title{left:100px;top:104px}
.post{top:180px;width:305px}
.post .meta{font-size:12.5px;color:var(--pink);margin-bottom:22px}
.post h3{font-family:"Playfair Display",serif;font-weight:500;font-size:21px;line-height:28px;color:var(--ink);margin-bottom:14px;max-width:295px}
.post p{font-size:13.5px;line-height:24.5px;color:var(--muted)}
.more{display:inline-flex;align-items:center;gap:8px;margin-top:14px;font-size:12.5px;color:var(--pink);text-transform:uppercase;font-weight:500}
.more i{width:22px;height:22px;border-radius:50%;border:1.5px solid var(--pink);display:inline-flex;align-items:center;justify-content:center}

/* community */
.community{top:1156px;height:944px;background:var(--navy);color:var(--white)}
.community .kicker{left:100px;top:110px;font-size:22px}
.community .kdot{left:365px;top:96px;width:12px;height:12px;border-radius:50%;background:var(--pink)}
.community h2{font-family:"Playfair Display",serif;font-weight:600;font-size:54px;line-height:1.1}
.community .h-people{left:100px;top:148px}
.community .p-people{left:100px;top:228px;width:440px;font-size:15px;line-height:28.5px}
.community .more-people{left:100px;top:382px;color:var(--pink)}
.community .more-people i{background:var(--white);border-color:var(--white)}
.community .h-consult{left:100px;top:478px;width:520px;line-height:64px}
.community .p-consult{left:100px;top:612px;width:440px;font-size:15px;line-height:28.5px}
.perk{left:622px;width:480px;display:flex;gap:22px}
.perk .ic{flex:0 0 88px;height:88px;border-radius:50%;border:1.5px solid var(--white);display:flex;align-items:center;justify-content:center}
.perk .ic.solid{background:var(--pink);border-color:var(--pink)}
.perk h4{font-size:20px;font-weight:600;margin-top:30px}
.perk p{font-size:14.5px;line-height:29px;margin-top:12px}

/* events */
.events{top:2100px;height:655px;background:linear-gradient(180deg,#f0b0ac,#eca4a0);overflow:hidden}
.events .ring{left:104px;top:40px;width:96px;height:96px;border-radius:50%;border:2px solid rgba(255,255,255,.35)}
.events h2{left:0;width:1200px;top:44px;text-align:center;font-family:"Playfair Display",serif;font-weight:600;font-size:50px;color:var(--white)}
.event{top:133px;width:484px;height:445px;background:var(--white);border-radius:4px;overflow:hidden;box-shadow:0 6px 20px rgba(120,40,40,.12)}
.event .art{height:287px}
.event h3{font-size:21px;font-weight:600;color:var(--ink);padding:20px 9px 6px}
.event p{font-size:13.5px;line-height:23px;color:var(--muted);padding:0 13px}

/* organisations */
.orgs{top:2755px;height:563px;background:var(--blush)}
.orgs h2{left:0;width:1200px;top:78px;text-align:center;font-family:"Playfair Display",serif;font-weight:500;font-size:52px;color:var(--ink)}
.grid{left:100px;top:177px;width:1004px;display:grid;grid-template-columns:repeat(5,1fr)}
.grid div{height:108px;display:flex;align-items:center;justify-content:center;gap:8px;font-size:19px;font-weight:500;color:#4a4680;border-right:1px solid var(--line);border-bottom:1px solid var(--line)}
.grid div:nth-child(5n){border-right:none}
.grid div:nth-child(n+11){border-bottom:none}
.grid div:nth-child(14){border-right:none}
.grid b{width:12px;height:12px;border-radius:50%;background:#4a4680;display:inline-block}

/* testimonials */
.clients{top:3318px;height:594px;background:var(--white)}
.clients .dot{left:100px;top:84px}
.clients .section-title{left:100px;top:100px;font-size:36px}
.arrow{top:101px;width:48px;height:48px;border-radius:50%;display:flex;align-items:center;justify-content:center}
.arrow.prev{left:997px;border:1.5px solid #cfcbd8}
.arrow.next{left:1055px;background:var(--navy)}
.quote{top:195px;width:472px;min-height:310px;background:var(--white);border:1px solid #eee;border-radius:6px;box-shadow:0 4px 16px rgba(0,0,0,.06);padding:0 24px 18px;display:flex;flex-direction:column}
.quote .mark{font-family:"Playfair Display",serif;font-weight:700;font-size:100px;line-height:1;color:var(--orange);height:58px;margin:-4px 0 0 -2px}
.quote blockquote{font-size:14px;font-style:italic;line-height:27px;color:var(--muted);margin-top:14px}
.quote .foot{margin-top:auto;padding-top:14px;display:flex;justify-content:space-between;align-items:flex-end}
.quote .who strong{display:block;font-size:16px;font-weight:500;color:var(--orange)}
.quote .who span{font-size:13px;color:var(--muted)}
.quote .org{font-size:24px;font-weight:600;color:#5a2d91;margin-bottom:6px}

/* footer */
.footer{top:3912px;height:458px;background:var(--navy);color:var(--white)}
.footer .flogo{left:108px;top:170px;font-family:"Playfair Display",serif;font-weight:700;font-size:96px;line-height:1;letter-spacing:-2px}
.social{top:298px;width:40px;height:40px;border-radius:50%;border:1.5px solid var(--white)}
.fcol{top:112px}
.fcol h5{font-size:16.5px;font-weight:500;margin-bottom:16px}
.fcol a{display:block;color:var(--white);text-decoration:none;font-size:14px;line-height:33px}
.vline{top:118px;width:1px;height:200px;background:rgba(255,255,255,.35)}
.contact{left:852px;top:112px;width:250px}
.contact h5{font-size:16.5px;font-weight:500;margin-bottom:16px}
.contact .row{display:flex;gap:8px;font-size:14px;line-height:20px;margin-bottom:18px}
.contact svg{flex:0 0 14px;margin-top:3px}
.footer .rule{left:100px;top:385px;width:1003px;height:1px;background:rgba(255,255,255,.3)}
.footer .copy{left:100px;top:410px;font-size:14px}
.footer .legal{left:852px;width:251px;top:410px;font-size:14px;text-align:right}
</style>
</head>
<body>

<header class="hero">
  <div class="abs brand">vorlo.</div>
  <div class="abs menu-btn" aria-label="Menu"><span></span><span></span><span></span></div>
  <h1 class="abs">People With <span class="accent" style="color:#f5a49a">Expertise.</span></h1>
  <div class="abs rule"></div>
  <p class="abs">Great PR is built on excellent communication and strong relationships. That’s what we do. We offer strategic advice and hands-on advocacy support to ensure you are heard and understood by the public, media and stakeholders.</p>
</header>
<div class="abs down" aria-label="Scroll down">
  <svg width="20" height="20" viewBox="0 0 20 20" fill="none" stroke="#262261" stroke-width="2" stroke-linecap="round"><path d="M10 3v14M4 11l6 6 6-6"/></svg>
</div>

<section class="news">
  <div class="abs dot"></div>
  <h2 class="abs section-title">Latest News</h2>

  <article class="abs post" style="left:100px">
    <div class="meta">▣ May 2, 2022 &nbsp;|&nbsp; ● Clara Dunmore</div>
    <h3>Tips from the Newsroom</h3>
    <p>Tips from the newsroom - our June media workshop will be hosted by former Daily Post and Metro Tribune reporter Tessa Rowe and will focus on how to get your stories heard in today’s media environment.</p>
    <span class="more">Learn more <i><svg width="10" height="10" viewBox="0 0 10 10" fill="none" stroke="#f8b4b2" stroke-width="1.5"><path d="M1 5h8M6 2l3 3-3 3"/></svg></i></span>
  </article>

  <article class="abs post" style="left:453px">
    <div class="meta">▣ May 2, 2022 &nbsp;|&nbsp; ● Clara Dunmore</div>
    <h3>Have you heard the news? The press release is (mostly) dead.</h3>
    <p>It was once believed that a concise, formally-toned paragraph was the key to a successful media outreach. But these days there are better ways to go about marketing your cause.</p>
    <span class="more">Learn more <i><svg width="10" height="10" viewBox="0 0 10 10" fill="none" stroke="#f8b4b2" stroke-width="1.5"><path d="M1 5h8M6 2l3 3-3 3"/></svg></i></span>
  </article>

  <article class="abs post" style="left:806px">
    <div class="meta">▣ May 2, 2022 &nbsp;|&nbsp; ● Clara Dunmore</div>
    <h3>Get the most out of your<br>comms in 2022</h3>
    <p>In 2022, the impact of the pandemic continues to touch every aspect of life and business in Aotearoa. With the right angle directed at the right news outlet, your story has a chance of getting cut-through.</p>
    <span class="more">Learn more <i><svg width="10" height="10" viewBox="0 0 10 10" fill="none" stroke="#f8b4b2" stroke-width="1.5"><path d="M1 5h8M6 2l3 3-3 3"/></svg></i></span>
  </article>
</section>

<section class="community">
  <div class="abs kicker">Join the Vorlo community</div>
  <div class="abs kdot"></div>
  <h2 class="abs h-people">People With <span class="accent">Vorlo</span></h2>
  <p class="abs p-people">Collaboration comes with plenty of benefits; flexibility, inspirational and thought-provoking projects and the opportunity to share expertise where it makes an impact. Our clients can build bespoke teams, fast-track big projects, and have an independent sounding board.</p>
  <span class="abs more more-people">Learn more <i><svg width="10" height="10" viewBox="0 0 10 10" fill="none" stroke="#262261" stroke-width="1.5"><path d="M1 5h8M6 2l3 3-3 3"/></svg></i></span>

  <h2 class="abs h-consult">Becoming a <span class="accent">Vorlo consultant.</span></h2>
  <p class="abs p-consult">People with Vorlo is designed to keep you in control while providing you a platform and professional profile no matter where you are at in the workforce. Five hours a day or five hours a month, we support senior consultants to create a work life that works for them.</p>

  <div class="abs perk" style="top:482px">
    <div class="ic"><svg width="40" height="36" viewBox="0 0 40 36" fill="none" stroke="#fff" stroke-width="1.6"><rect x="3" y="14" width="34" height="4"/><path d="M6 18v16M34 18v16"/><rect x="12" y="3" width="16" height="10"/><rect x="22" y="20" width="10" height="10"/></svg></div>
    <div><h4>Work in your wheelhouse.</h4></div>
  </div>
  <div class="abs perk" style="top:596px">
    <div class="ic"><svg width="34" height="38" viewBox="0 0 34 38" fill="none" stroke="#fff" stroke-width="1.6"><rect x="5" y="5" width="24" height="30" rx="2"/><path d="M12 5V2h10v3"/><path d="M11 20l4 4 8-8"/></svg></div>
    <div><h4>We cover you.</h4></div>
  </div>
  <div class="abs perk" style="top:706px">
    <div class="ic solid"><svg width="40" height="38" viewBox="0 0 40 38" fill="none" stroke="#fff" stroke-width="1.6"><circle cx="20" cy="9" r="6"/><circle cx="8" cy="27" r="6"/><circle cx="32" cy="27" r="6"/></svg></div>
    <div><h4 style="margin-top:8px">Wraparound support.</h4><p>Working with us means working as a team, with other consultants to call upon for brainstorming sessions, mentoring and reviewing.</p></div>
  </div>
</section>

<section class="events">
  <div class="abs ring"></div>
  <h2 class="abs">Upcoming Events</h2>
  <article class="abs event" style="left:100px">
    <div class="art" role="img" aria-label="Workshop promo graphic: Why journalists don't like press releases, with event date" style="background:linear-gradient(90deg,#3b3866 0%,#4a4676 40%,#f0922a 60%,#f7931d 100%)"></div>
    <h3>Tips From The Newsroom Media Workshop</h3>
    <p>Join former senior editor and journalist Tessa Rowe for this interactive Media 101 workshop. Tessa has been in &amp; around media for a decade, has an eye for a story angle &amp; the experience to know how best to pitch it.</p>
  </article>
  <article class="abs event" style="left:618px">
    <div class="art" role="img" aria-label="Illustration of a writer working at a laptop beside stacks of books" style="background:linear-gradient(180deg,#f4d7a0,#e9b46d 70%,#b99a86)"></div>
    <h3>BIM writing 101</h3>
    <p>Election season starts early in politics, and before you know it, it’s BIM time again.</p>
  </article>
</section>

<section class="orgs">
  <h2 class="abs">Organisations With Vorlo</h2>
  <div class="abs grid">
    <div>Kinfolk Hub</div>
    <div><b></b>Case Review Panel</div>
    <div>Hapori Net</div>
    <div>Transit Office</div>
    <div><b></b>Fairness Office</div>
    <div><b></b>RoadAhead</div>
    <div>calma</div>
    <div>Westwood</div>
    <div>Idea Room</div>
    <div>Kiwi Wings</div>
    <div>Coastline Minerals</div>
    <div><b></b>Harlow Trust</div>
    <div>TrueNorth</div>
    <div>Forest Fund</div>
  </div>
</section>

<section class="clients">
  <div class="abs dot"></div>
  <h2 class="abs section-title">What Our Clients Say</h2>
  <div class="abs arrow prev" aria-label="Previous"><svg width="14" height="14" viewBox="0 0 14 14" fill="none" stroke="#9d99ad" stroke-width="1.6"><path d="M9 2L4 7l5 5"/></svg></div>
  <div class="abs arrow next" aria-label="Next"><svg width="14" height="14" viewBox="0 0 14 14" fill="none" stroke="#fff" stroke-width="1.6"><path d="M5 2l5 5-5 5"/></svg></div>

  <figure class="abs quote" style="left:100px">
    <div class="mark">“</div>
    <blockquote>“With their depth of knowledge and experience Clara and the Vorlo team have provided Calma Trust with invaluable guidance as we represent our community. We are so grateful for their professionalism and expertise, enabling us to advocate for those suffering while we carry out our vital work of supporting families.”</blockquote>
    <div class="foot">
      <figcaption class="who"><strong>Jenna Hart</strong><span>Chair, Calma Trust</span></figcaption>
      <div class="org">calma</div>
    </div>
  </figure>
  <figure class="abs quote" style="left:630px">
    <div class="mark">“</div>
    <blockquote>“With their depth of knowledge and experience Clara and the Vorlo team have provided Calma Trust with invaluable guidance as we represent our community. We are so grateful for their professionalism and expertise, enabling us to advocate for those suffering while we carry out our vital work of supporting families.”</blockquote>
    <div class="foot">
      <figcaption class="who"><strong>Jenna Hart</strong><span>Chair, Calma Trust</span></figcaption>
      <div class="org">calma</div>
    </div>
  </figure>
</section>

<footer class="footer">
  <div class="abs flogo">vorlo.</div>
  <span class="abs social" style="left:100px" aria-label="Social link"></span>
  <span class="abs social" style="left:155px" aria-label="Social link"></span>
  <span class="abs social" style="left:209px" aria-label="Social link"></span>
  <span class="abs social" style="left:262px" aria-label="Social link"></span>

  <div class="abs vline" style="left:387px"></div>
  <nav class="abs fcol" style="left:434px">
    <h5>Quick Link</h5>
    <a href="#">Home</a><a href="#">About Us</a><a href="#">Our Platform</a><a href="#">Our Team</a><a href="#">Investment Portfolio</a><a href="#">Contact us</a>
  </nav>
  <div class="abs vline" style="left:621px"></div>
  <nav class="abs fcol" style="left:667px">
    <h5>Other Link</h5>
    <a href="#">Who We Are</a><a href="#">Career</a><a href="#">News</a><a href="#">Resources</a><a href="#">Contact</a>
  </nav>
  <div class="abs vline" style="left:799px"></div>
  <div class="abs contact">
    <h5>Contact Info</h5>
    <div class="row"><svg width="14" height="16" viewBox="0 0 14 16" fill="#fff"><path d="M7 0a6 6 0 0 0-6 6c0 4.5 6 10 6 10s6-5.5 6-10a6 6 0 0 0-6-6zm0 8.5A2.5 2.5 0 1 1 7 3.5a2.5 2.5 0 0 1 0 5z"/></svg><span>Kestrel House Level 2, 40 Harbour St Wellington 6011</span></div>
    <div class="row"><svg width="14" height="14" viewBox="0 0 14 14" fill="none" stroke="#fff" stroke-width="1.4"><path d="M3 1l2.5 3-1.5 1.5a8 8 0 0 0 4.5 4.5L10 8.5l3 2.5-1.5 2C6 13 1 8 1 2.5z"/></svg><span>Mara 022 000 1234<br>Clara 021 000 5678</span></div>
    <div class="row"><svg width="14" height="12" viewBox="0 0 14 12" fill="#fff"><path d="M0 1h14v10H0z"/><path d="M0 1l7 5 7-5" stroke="#262261" stroke-width="1.2" fill="none"/></svg><span>hello@vorlo.co.nz</span></div>
  </div>

  <div class="abs rule"></div>
  <div class="abs copy">Copyright © 2022 - Vorlo Communications Limited. All Right Reserved</div>
  <div class="abs legal">Privacy Policy &nbsp;|&nbsp; Terms &amp; Conditions</div>
</footer>

</body>
</html>
```